Photography blog homepage design

I need a new webpage design for my photography blog. My blog focuses on post-processing techniques, particularly in luminosity masking, HDR photography and other advanced photo editing skills. I want the new homepage to let visitors know instantly what the blog is about as this is currently not very obvious from the feedback I received. Apart from that, the homepage should also inform/showcase latest blog post and/or popular blog post and/or some of the training courses I offer (that's my idea, but I leave it to your expertise). There should also ideally have a CTA that leads visitors to the "Start Here" page where they can learn more about my blog. The bulk of my audience is intermediate/advanced photographers who are above 30-35 years old, with a significant group in the 60 to >75 age group. The design should convey trust and creativity at the same time. The color theme for my blog is orange and dark grey. URL is www.lumbrakest.com, you can use the current content on that page.

Target Market(s)

Intermediate/advanced photographers (hobbyist or professional) age 35-75 years old.

Number of Pages Required

1 page

Font styles to use
Sans Serif

Colors
faa54b
f68e4e
f78f20

Requirements
Must have
• Upside down homepage (menus at the bottom)

```html
<!DOCTYPE html>
<html lang="en">
<head>
<meta charset="utf-8">
<title>Lumbrakest — Homepage Desktop and Mobile</title>
<link href="https://fonts.googleapis.com/css2?family=Montserrat:wght@400;500;600;700;800&family=Playfair+Display:ital,wght@0,400;0,700;1,400&display=swap" rel="stylesheet">
<style>
:root{
  --board:#454545;
  --orange:#f78f20;
  --orange-soft:#f68e4e;
  --ink:#222;
  --body:#444;
  --muted:#888;
  --light:#f4f4f4;
  --white:#fff;
  --footer:#3a3a3a;
}
*{box-sizing:border-box;margin:0;padding:0}
html,body{width:1200px;height:3000px;overflow:hidden}
body{background:var(--board);font-family:'Montserrat',sans-serif;color:var(--body);position:relative}
.board-label{position:absolute;top:76px;color:#f2f2f2;font-weight:600;font-size:20px;letter-spacing:.2px}
.frame{position:absolute;top:144px;background:var(--white);overflow:hidden}
.frame--desktop{left:99px;width:708px;height:1918px}
.frame--mobile{left:858px;width:239px;height:2856px}
.abs{position:absolute}
.topbar{left:0;right:0;top:0;background:var(--light);display:flex;justify-content:space-between;align-items:center;font-size:5px;letter-spacing:.4px;color:#666;text-transform:uppercase}
.socials{display:flex;gap:5px}
.socials span{width:5px;height:5px;border-radius:50%;background:#777;display:block}
.brandbar{left:0;right:0;display:flex;justify-content:center;align-items:center;gap:4px}
.brand{font-weight:800;color:var(--ink);letter-spacing:-.3px}
.brand-dot{border-radius:50%;background:var(--orange)}
.hero{left:0;right:0;background:linear-gradient(180deg,#5c6160 0%,#4a504d 35%,#2f3a31 70%,#242b24 100%);color:#fff;text-align:center}
.hero h1{font-weight:600;letter-spacing:.5px}
.btn{display:inline-flex;align-items:center;justify-content:center;gap:8px;background:var(--orange);color:#fff;font-weight:600}
.btn svg{display:block}
.photo{border-radius:0}
.serif{font-family:'Playfair Display',serif}
.author{text-align:center}
.author .name{font-family:'Playfair Display',serif;color:#333}
.author .role{font-family:'Playfair Display',serif;font-style:italic;color:var(--muted)}
.story p{margin-bottom:7px}
.story b{color:#222}
.section-title{font-family:'Playfair Display',serif;font-weight:700;color:#222;text-align:center}
.rule{background:#bbb;height:1px}
.card{background:#fff;text-align:center;display:flex;flex-direction:column;align-items:center}
.card h3{font-weight:600;color:#222}
.card p{color:#555}
.pill{border:1px solid #333;border-radius:20px;color:#222;font-weight:600;display:inline-block}
.post .date{font-family:'Playfair Display',serif;font-style:italic;color:#777}
.post h4{font-family:'Playfair Display',serif;font-weight:700;color:#222}
.post p{color:#555}
.press{display:flex;justify-content:center;align-items:center;gap:14px}
.press span{display:block;background:#8a8a8a;border-radius:2px}
.footer{left:0;right:0;background:var(--footer);display:flex;justify-content:center;align-items:center;gap:26px;color:#fff;font-weight:600;font-size:7px;letter-spacing:.4px}
.chat{border-radius:50%;background:var(--orange);display:flex;align-items:center;justify-content:center}
</style>
</head>
<body>

<div class="board-label" style="left:108px">Desktop version</div>
<div class="board-label" style="left:862px">Mobile version</div>

<!-- Desktop -->
<main class="frame frame--desktop">
  <div class="abs topbar" style="height:13px;padding:0 140px 0 139px"><span>Welcome to Lumbrakest</span><div class="socials"><span></span><span></span><span></span><span></span></div></div>
  <div class="abs brandbar" style="top:13px;height:43px"><span class="brand" style="font-size:14px">LUMBRAKEST</span><span class="brand-dot" style="width:7px;height:7px"></span></div>

  <section class="abs hero" role="img" aria-label="Misty pine forest on a foggy hillside" style="top:56px;height:205px;padding-top:46px">
    <h1 style="font-size:15.5px;line-height:22px">Discover How To Be More Productive In<br>Editing Without Spending More Time</h1>
    <p style="font-size:7.5px;line-height:13px;margin-top:6px">Download the free 4-Step Editing Framework ebook. Use the PRISM framework to<br>boost your creativity and productivity.</p>
    <a class="btn" style="margin-top:10px;width:100px;height:24px;font-size:7px">Free Download <svg width="10" height="6" viewBox="0 0 10 6"><path d="M0 3h8M6 1l2 2-2 2" stroke="#fff" fill="none" stroke-width="1"/></svg></a>
  </section>

  <article class="abs story" style="left:139px;top:296px;width:218px;font-size:6.5px;line-height:9px">
    <p>Let me ask you this:</p>
    <p><b>How many cameras and lenses have you owned?</b></p>
    <p>I have a Vantor 24-70 f/2.8 in my inventory. I bought it from TradeNook because I had read good reviews about it.</p>
    <p><b>But guess what...?</b></p>
    <p>Apart from doing some test shots, it's been sitting on my shelf collecting dust ever since. I thought of selling it but never had the will to take photos, list it and all that.</p>
    <p>I also have a bunch of M42 lenses stored in another camera bag which I probably will never use them.</p>
    <p>These are just a few examples...I had even more lenses that have come and gone. Thinking back, I wasted a lot of money on gadget.</p>
    <p>As I gain more experience in photography, I learned that I don't need the best gear to produce good images...what I need is editing style!</p>
    <p>I also discovered that a good photo is 70% editing, 25% camera skills and 5% of luck!</p>
    <p><b>What did I change?</b></p>
    <p>I redirected my focus...invested more in developing a unique editing style.</p>
    <p>...and that, my friend, is one of the best decisions I have ever made!</p>
  </article>
  <div class="abs photo" role="img" aria-label="Portrait of the author in a grey t-shirt" style="left:366px;top:304px;width:205px;height:218px;background:linear-gradient(180deg,#fff 0%,#f3f3f3 40%,#8a8d92 75%,#6e7177 100%)"></div>
  <div class="abs author" style="left:366px;top:536px;width:205px"><div class="name" style="font-size:13px">Daren Holt</div><div class="role" style="font-size:7px;margin-top:2px">Author of Lumbrakest</div></div>

  <p class="abs" style="left:0;right:0;top:596px;text-align:center;font-size:6.5px;line-height:11px">If you've been neglecting image editing...it's time to take action now and invest more effort.<br><b style="color:#222">Download The 4-Step Editing Framework to get started!</b></p>
  <div class="abs" role="img" aria-label="Before and after edit of a frosty meadow at sunset" style="left:233px;top:631px;width:242px;height:162px;background:linear-gradient(90deg,#c9cfd6 0%,#9aa6b8 48%,#fff 49.6%,#fff 50.4%,#7e7c9c 51%,#5c6a93 100%)"></div>
  <p class="abs" style="left:0;right:0;top:811px;text-align:center;font-size:6.5px">Want to know how to transform images like this? Click the green button below to download your free ebook!</p>
  <a class="abs btn" style="left:295px;top:835px;width:100px;height:25px;font-size:7px">Get Free ebook <svg width="10" height="6" viewBox="0 0 10 6"><path d="M0 3h8M6 1l2 2-2 2" stroke="#fff" fill="none" stroke-width="1"/></svg></a>

  <section class="abs" style="left:0;right:0;top:896px;height:265px;background:var(--light)">
    <h2 class="section-title" style="font-size:12.5px;margin-top:30px">What do you need help with?</h2>
    <div class="abs card" style="left:139px;top:76px;width:137px;height:157px;padding-top:20px">
      <svg width="38" height="38" viewBox="0 0 38 38"><circle cx="18" cy="18" r="18" fill="#f78f20"/><circle cx="14" cy="13" r="3" fill="none" stroke="#111" stroke-width="1.3"/><path d="M8 30l9-12 5 7 4-5 8 10z" fill="none" stroke="#111" stroke-width="1.3"/></svg>
      <h3 style="font-size:9.5px;margin-top:8px">Luminosity Masks</h3>
      <p style="font-size:6px;line-height:9px;margin:6px 12px 0">Want to learn luminosity masking but find it too hard? Signup to the free luminosity masks crash course.</p>
      <span class="pill" style="font-size:6px;padding:3px 10px;margin-top:8px">LM Crash Course</span>
    </div>
    <div class="abs card" style="left:286px;top:76px;width:137px;height:157px;padding-top:20px">
      <svg width="38" height="38" viewBox="0 0 38 38"><circle cx="18" cy="18" r="18" fill="#f78f20"/><rect x="9" y="10" width="19" height="16" rx="2" fill="none" stroke="#111" stroke-width="1.3"/><path d="M10 24l6-7 5 5 3-3 4 4" fill="none" stroke="#111" stroke-width="1.3"/><circle cx="29" cy="28" r="5" fill="#f4f4f4" stroke="#111" stroke-width="1.3"/><path d="M29 25.5v5M26.5 28h5" stroke="#111" stroke-width="1.3"/></svg>
      <h3 style="font-size:9.5px;margin-top:8px">Histograms</h3>
      <p style="font-size:6px;line-height:9px;margin:6px 12px 0">Struggling to get the right exposure? Master histograms with this ebook to help you nail the exposure in every shot.</p>
      <span class="pill" style="font-size:6px;padding:3px 10px;margin-top:8px">Dissecting Histogram</span>
    </div>
    <div class="abs card" style="left:434px;top:76px;width:137px;height:157px;padding-top:20px">
      <svg width="38" height="38" viewBox="0 0 38 38"><circle cx="18" cy="18" r="18" fill="#f78f20"/><rect x="8" y="8" width="18" height="15" fill="none" stroke="#111" stroke-width="1.3"/><rect x="11" y="11" width="18" height="15" fill="#f78f20" stroke="#111" stroke-width="1.3"/><rect x="14" y="14" width="18" height="15" fill="#f78f20" stroke="#111" stroke-width="1.3"/><path d="M15 27l6-6 4 4 3-2 4 4" fill="none" stroke="#111" stroke-width="1.3"/></svg>
      <h3 style="font-size:9.5px;margin-top:8px">Exposure Blending</h3>
      <p style="font-size:6px;line-height:9px;margin:6px 12px 0">Stop producing mediocre HDR. Get the HDX Blueprint to start creating natural looking HDR images.</p>
      <span class="pill" style="font-size:6px;padding:3px 10px;margin-top:8px">The HDX Blueprint</span>
    </div>
  </section>

  <section class="abs" style="left:0;right:0;top:1161px;height:538px">
    <h2 class="section-title" style="font-size:12.5px;margin-top:31px">Latest Photography News</h2>
    <div class="abs rule" style="left:316px;width:76px;top:56px"></div>

    <div class="abs" role="img" aria-label="Aerial view of a river winding through green forest" style="left:139px;top:89px;width:121px;height:155px;background:linear-gradient(135deg,#3f5a3a,#6f8f52 45%,#2f4e5e 60%,#56743f)"></div>
    <div class="abs post" style="left:268px;top:156px;width:80px"><div class="date" style="font-size:6px">07/12/2019</div><h4 style="font-size:8px;line-height:10px;margin-top:4px">Lorem ipsum dolor sit amet, consectetur adipiscing elit.</h4><p style="font-size:6px;line-height:8px;margin-top:5px">Vivamus et maximus nisi. Nulla sit amet gravida neque. Sed sed aliquam lectus. Nulla lacinia sit amet diam a auctor.</p></div>

    <div class="abs" role="img" aria-label="Portrait of a woman among dark foliage" style="left:360px;top:119px;width:121px;height:155px;background:linear-gradient(180deg,#1f2a22,#3a3f35 50%,#1a1f1a)"></div>
    <div class="abs post" style="left:489px;top:186px;width:80px"><div class="date" style="font-size:6px">07/12/2019</div><h4 style="font-size:8px;line-height:10px;margin-top:4px">Lorem ipsum dolor sit amet, consectetur adipiscing elit.</h4><p style="font-size:6px;line-height:8px;margin-top:5px">Vivamus et maximus nisi. Nulla sit amet gravida neque. Sed sed aliquam lectus. Nulla lacinia sit amet diam a auctor.</p></div>

    <div class="abs" role="img" aria-label="Curved orange sandstone canyon walls" style="left:139px;top:273px;width:121px;height:155px;background:linear-gradient(135deg,#e88a5a,#f7c9a6 40%,#d96a3c 70%,#f2b48c)"></div>
    <div class="abs post" style="left:268px;top:340px;width:80px"><div class="date" style="font-size:6px">07/12/2019</div><h4 style="font-size:8px;line-height:10px;margin-top:4px">Lorem ipsum dolor sit amet, consectetur adipiscing elit.</h4><p style="font-size:6px;line-height:8px;margin-top:5px">Vivamus et maximus nisi. Nulla sit amet gravida neque. Sed sed aliquam lectus. Nulla lacinia sit amet diam a auctor.</p></div>

    <div class="abs" role="img" aria-label="Person in a dark coat standing in an autumn forest" style="left:360px;top:303px;width:121px;height:155px;background:linear-gradient(180deg,#6a5d4c,#4e4536 55%,#3a3328)"></div>
    <div class="abs post" style="left:489px;top:370px;width:80px"><div class="date" style="font-size:6px">07/12/2019</div><h4 style="font-size:8px;line-height:10px;margin-top:4px">Lorem ipsum dolor sit amet, consectetur adipiscing elit.</h4><p style="font-size:6px;line-height:8px;margin-top:5px">Vivamus et maximus nisi. Nulla sit amet gravida neque. Sed sed aliquam lectus. Nulla lacinia sit amet diam a auctor.</p></div>

    <a class="abs" style="left:311px;top:486px;width:88px;height:22px;border:1px solid #333;display:flex;align-items:center;justify-content:center;font-size:6.5px;font-weight:600;color:#222">LOAD MORE</a>
  </section>

  <section class="abs" style="left:0;right:0;top:1699px;height:157px;background:var(--light)">
    <h2 class="section-title" style="font-size:12.5px;margin-top:30px">Published On</h2>
    <div class="abs rule" style="left:316px;width:76px;top:54px"></div>
    <div class="abs press" style="left:0;right:0;top:82px"><span style="width:52px;height:14px"></span><span style="width:56px;height:14px"></span><span style="width:30px;height:18px"></span><span style="width:50px;height:14px"></span><span style="width:74px;height:14px"></span><span style="width:30px;height:18px"></span></div>
    <div class="abs press" style="left:0;right:0;top:114px"><span style="width:44px;height:22px"></span><span style="width:94px;height:12px"></span><span style="width:82px;height:10px"></span><span style="width:84px;height:12px"></span></div>
  </section>

  <nav class="abs footer" style="top:1856px;height:62px"><span>START HERE</span><span>BLOG</span><span>TUTORIALS</span><span>ABOUT</span></nav>
  <div class="abs chat" style="left:646px;top:1870px;width:36px;height:36px"><svg width="16" height="14" viewBox="0 0 16 14"><rect x="1" y="1" width="14" height="9" rx="2" fill="none" stroke="#fff" stroke-width="1.3"/><path d="M4 10v3l3-3" fill="none" stroke="#fff" stroke-width="1.3"/><circle cx="5" cy="5.5" r=".9" fill="#fff"/><circle cx="8" cy="5.5" r=".9" fill="#fff"/><circle cx="11" cy="5.5" r=".9" fill="#fff"/></svg></div>
</main>

<!-- Mobile -->
<main class="frame frame--mobile">
  <div class="abs topbar" style="height:19px;padding:0 8px 0 11px;font-size:5.5px"><span>Welcome to Lumbrakest</span><div class="socials"><span style="width:6px;height:6px"></span><span style="width:6px;height:6px"></span><span style="width:6px;height:6px"></span><span style="width:6px;height:6px"></span></div></div>
  <div class="abs brandbar" style="top:19px;height:55px"><span class="brand" style="font-size:18px">LUMBRAKEST</span><span class="brand-dot" style="width:8px;height:8px"></span></div>

  <section class="abs hero" role="img" aria-label="Misty pine forest on a foggy hillside" style="top:74px;height:279px;padding-top:76px">
    <h1 style="font-size:10.5px;line-height:17px">Discover How To Be More<br>Productive In Editing Without<br>Spending More Time</h1>
    <p style="font-size:5.8px;line-height:9.5px;margin-top:6px">Download the free 4-Step Editing Framework<br>ebook. Use the PRISM framework to boost your<br>creativity and productivity.</p>
    <a class="btn" style="margin-top:20px;width:76px;height:18px;font-size:5.5px">Free Download <svg width="8" height="5" viewBox="0 0 10 6"><path d="M0 3h8M6 1l2 2-2 2" stroke="#fff" fill="none" stroke-width="1"/></svg></a>
  </section>

  <div class="abs photo" role="img" aria-label="Portrait of the author in a grey t-shirt" style="left:47px;top:381px;width:149px;height:158px;background:linear-gradient(180deg,#fff 0%,#f3f3f3 40%,#8a8d92 75%,#6e7177 100%)"></div>
  <div class="abs author" style="left:0;right:0;top:549px"><div class="name" style="font-size:16px">Daren Holt</div><div class="role" style="font-size:9px;margin-top:2px">Author of Lumbrakest</div></div>

  <article class="abs story" style="left:11px;top:606px;width:218px;font-size:8.4px;line-height:12px">
    <p style="margin-bottom:12px">Let me ask you this:</p>
    <p style="margin-bottom:12px"><b>How many cameras and lenses have you owned?</b></p>
    <p style="margin-bottom:12px">I have a Vantor 24-70 f/2.8 in my inventory. I bought it from TradeNook because I had read good reviews about it.</p>
    <p style="margin-bottom:12px"><b>But guess what...?</b></p>
    <p style="margin-bottom:12px">Apart from doing some test shots, it's been sitting on my shelf collecting dust ever since. I thought of selling it but never had the will to take photos, list it and all that.</p>
    <p style="margin-bottom:12px">I also have a bunch of M42 lenses stored in another camera bag which I probably will never use them.</p>
    <p style="margin-bottom:12px">These are just a few examples...I had even more lenses that have come and gone. Thinking back, I wasted a lot of money on gadget.</p>
    <p style="margin-bottom:12px">As I gain more experience in photography, I learned that I don't need the best gear to produce good images...what I need is editing style!</p>
    <p style="margin-bottom:12px">I also discovered that a good photo is 70% editing, 25% camera skills and 5% of luck!</p>
    <p style="margin-bottom:12px"><b>What did I change?</b></p>
    <p style="margin-bottom:12px">I redirected my focus...invested more in developing a unique</p>
  </article>
  <p class="abs" style="left:0;right:0;top:1068px;text-align:center;font-size:8.4px;line-height:15px">If you've been neglecting image editing...it's time<br>to take action now and invest more effort.<br><b style="color:#222">Download The 4-Step Editing Framework to<br>get started!</b></p>

  <div class="abs" role="img" aria-label="Before and after edit of a frosty meadow at sunset" style="left:9px;top:1143px;width:219px;height:145px;background:linear-gradient(90deg,#c9cfd6 0%,#9aa6b8 48%,#fff 49.6%,#fff 50.4%,#7e7c9c 51%,#5c6a93 100%)"></div>
  <p class="abs" style="left:0;right:0;top:1302px;text-align:center;font-size:8.4px;line-height:15px">Want to know how to transform images like this?<br>Click the green button below to download your<br>free ebook!</p>
  <a class="abs btn" style="left:72px;top:1359px;width:83px;height:20px;font-size:5.8px">Get Free ebook <svg width="8" height="5" viewBox="0 0 10 6"><path d="M0 3h8M6 1l2 2-2 2" stroke="#fff" fill="none" stroke-width="1"/></svg></a>

  <section class="abs" style="left:0;right:0;top:1411px;height:806px;background:var(--light)">
    <h2 class="section-title" style="font-size:15px;margin-top:33px">What do you need help with?</h2>
    <div class="abs card" style="left:26px;top:93px;width:186px;height:213px;padding-top:27px">
      <svg width="52" height="52" viewBox="0 0 38 38"><circle cx="18" cy="18" r="18" fill="#f78f20"/><circle cx="14" cy="13" r="3" fill="none" stroke="#111" stroke-width="1.3"/><path d="M8 30l9-12 5 7 4-5 8 10z" fill="none" stroke="#111" stroke-width="1.3"/></svg>
      <h3 style="font-size:13px;margin-top:11px">Luminosity Masks</h3>
      <p style="font-size:8px;line-height:13px;margin:6px 14px 0">Want to learn luminosity masking but find it too hard? Signup to the free luminosity masks crash course.</p>
      <span class="pill" style="font-size:8px;padding:5px 14px;margin-top:11px">LM Crash Course</span>
    </div>
    <div class="abs card" style="left:26px;top:320px;width:186px;height:213px;padding-top:27px">
      <svg width="52" height="52" viewBox="0 0 38 38"><circle cx="18" cy="18" r="18" fill="#f78f20"/><rect x="9" y="10" width="19" height="16" rx="2" fill="none" stroke="#111" stroke-width="1.3"/><path d="M10 24l6-7 5 5 3-3 4 4" fill="none" stroke="#111" stroke-width="1.3"/><circle cx="29" cy="28" r="5" fill="#f4f4f4" stroke="#111" stroke-width="1.3"/><path d="M29 25.5v5M26.5 28h5" stroke="#111" stroke-width="1.3"/></svg>
      <h3 style="font-size:13px;margin-top:11px">Histograms</h3>
      <p style="font-size:8px;line-height:13px;margin:6px 14px 0">Struggling to get the right exposure? Master histograms with this ebook to help you nail the exposure in every shot.</p>
      <span class="pill" style="font-size:8px;padding:5px 14px;margin-top:11px">Dissecting Histogram</span>
    </div>
    <div class="abs card" style="left:26px;top:547px;width:186px;height:213px;padding-top:27px">
      <svg width="52" height="52" viewBox="0 0 38 38"><circle cx="18" cy="18" r="18" fill="#f78f20"/><rect x="8" y="8" width="18" height="15" fill="none" stroke="#111" stroke-width="1.3"/><rect x="11" y="11" width="18" height="15" fill="#f78f20" stroke="#111" stroke-width="1.3"/><rect x="14" y="14" width="18" height="15" fill="#f78f20" stroke="#111" stroke-width="1.3"/><path d="M15 27l6-6 4 4 3-2 4 4" fill="none" stroke="#111" stroke-width="1.3"/></svg>
      <h3 style="font-size:13px;margin-top:11px">Exposure Blending</h3>
      <p style="font-size:8px;line-height:13px;margin:6px 14px 0">Stop producing mediocre HDR. Get the HDX Blueprint to start creating natural looking HDR images.</p>
      <span class="pill" style="font-size:8px;padding:5px 14px;margin-top:11px">The HDX Blueprint</span>
    </div>
  </section>

  <section class="abs" style="left:0;right:0;top:2217px;height:639px">
    <h2 class="section-title" style="font-size:14.5px;margin-top:37px">Latest Photography News</h2>
    <div class="abs rule" style="left:75px;width:90px;top:67px"></div>
    <div class="abs" role="img" aria-label="Aerial view of a river winding through green forest" style="left:36px;top:101px;width:167px;height:212px;background:linear-gradient(135deg,#3f5a3a,#6f8f52 45%,#2f4e5e 60%,#56743f)"></div>
    <div class="abs post" style="left:36px;top:323px;width:120px"><div class="date" style="font-size:8.5px">07/12/2019</div><h4 style="font-size:11px;line-height:15px;margin-top:6px">Lorem ipsum dolor sit amet, consectetur adipiscing elit.</h4><p style="font-size:8.4px;line-height:12px;margin-top:8px">Vivamus et maximus nisi. Nulla sit amet gravida neque. Sed sed aliquam lectus. Nulla lacinia sit amet diam a auctor.</p></div>
    <div class="abs" role="img" aria-label="Portrait of a woman among dark foliage" style="left:36px;top:474px;width:167px;height:212px;background:linear-gradient(180deg,#1f2a22,#3a3f35 50%,#1a1f1a)"></div>
  </section>
</main>

</body>
</html>
```